Business Card Design

I need a business card for my Heating / Cooling Business. I've been in the business for 28 years. The name of the company is "Tom's Heating and Cooling".
Designers, I've attached an old business card we've used to copy the information.
Take off 15 years of experience
Industry/Entity Type
Business
Contact Information for Business Card
Gene Waltham and Lorna Waltham(740)-795-4758

```html
<!DOCTYPE html>
<html lang="en">
<head>
<meta charset="utf-8">
<title>Tom's Heating &amp; Air Conditioning — Business Card</title>
<link href="https://fonts.googleapis.com/css2?family=Baloo+2:wght@800&family=Open+Sans:wght@400;600&display=swap" rel="stylesheet">
<style>
  :root {
    --backdrop: #e4e5e8;
    --card: #ffffff;
    --brand-blue: #27339a;
    --band-start: #3c4fb8;
    --band-end: #1f2a8c;
    --body-grey: #5c5c5c;
    --divider: #8a93c8;
  }
  * { margin: 0; padding: 0; box-sizing: border-box; }
  html, body {
    width: 1200px;
    height: 901px;
    overflow: hidden;
    background: var(--backdrop);
  }
  .stage {
    width: 1200px;
    height: 901px;
    display: flex;
    align-items: center;
    justify-content: center;
  }
  .business-card {
    position: relative;
    width: 1000px;
    height: 571px;
    background: var(--card);
    box-shadow: 0 10px 30px rgba(0, 0, 0, 0.18);
    overflow: hidden;
  }
  .company-name {
    position: absolute;
    left: 150px;
    top: 112px;
    font-family: "Baloo 2", "Arial Rounded MT Bold", sans-serif;
    font-weight: 800;
    font-size: 52px;
    line-height: 1;
    color: var(--brand-blue);
    white-space: nowrap;
  }
  .owner-band {
    position: absolute;
    left: 90px;
    right: 0;
    top: 205px;
    height: 68px;
    background: linear-gradient(90deg, var(--band-start), var(--band-end));
    display: flex;
    align-items: center;
    padding-left: 130px;
  }
  .owner-names {
    font-family: "Open Sans", sans-serif;
    font-weight: 600;
    font-size: 36px;
    color: #ffffff;
    white-space: nowrap;
  }
  .services {
    position: absolute;
    left: 150px;
    top: 310px;
    font-family: "Open Sans", sans-serif;
    font-weight: 400;
    font-size: 21px;
    line-height: 1.45;
    color: var(--body-grey);
    white-space: nowrap;
  }
  .contact-line {
    position: absolute;
    left: 170px;
    top: 410px;
    display: flex;
    align-items: center;
    gap: 16px;
    font-family: "Open Sans", sans-serif;
    font-size: 19px;
    color: var(--body-grey);
    white-space: nowrap;
  }
  .contact-label {
    color: var(--brand-blue);
    font-weight: 600;
  }
  .contact-divider {
    width: 1px;
    height: 22px;
    background: var(--divider);
  }
</style>
</head>
<body>
  <main class="stage">
    <article class="business-card">
      <h1 class="company-name">Tom's heating &amp; Air Conditioning</h1>
      <div class="owner-band">
        <p class="owner-names">Gene Waltham and Lorna Waltham</p>
      </div>
      <p class="services">
        Installation And Service Small Appliance Repair Plumbing Refrigeration<br>
        And Car Air Conditioning Professional Mobile Home Installation
      </p>
      <p class="contact-line">
        <span><span class="contact-label">P:</span> (612)-438-2091</span>
        <span class="contact-divider"></span>
        <span>81270 maple lane cedar bluff, ohio 44210</span>
        <span class="contact-divider"></span>
        <span>certified repairman</span>
      </p>
    </article>
  </main>
</body>
</html>
```